Powerpoint template for Trivia Company

Revamp of our current powerpoint template to make it more professional and fun for the players. Something worthy of a trivia company. Please see logo attached for potential colour - but also open to other ideas.

NO BRANDING REQUIRED (IE: No mention of our company or logo on the template please)

Target Market(s)

Bars/restaurants

Colors
3176b5
00a990

```html
<!DOCTYPE html>
<html lang="en">
<head>
<meta charset="utf-8">
<title>Quiz Categories</title>
<link href="https://fonts.googleapis.com/css2?family=Bubblegum+Sans&display=swap" rel="stylesheet">
<style>
:root{
  --teal:#0aa79e;
  --teal-deep:#078a8c;
  --navy:#101a55;
  --indigo:#2b3f9e;
  --blue:#3176b5;
  --gold:#ffd500;
  --orange:#f6a531;
  --orange-deep:#ea8d1c;
  --rim:#c9ccd3;
  --white:#ffffff;
  --next-red:#f04a14;
}
*{margin:0;padding:0;box-sizing:border-box}
html,body{width:1200px;height:675px;overflow:hidden;background:var(--navy)}
.slide{position:relative;width:1200px;height:675px;overflow:hidden;font-family:"Bubblegum Sans",cursive}
.backdrop{position:absolute;inset:0;
  background:
    radial-gradient(ellipse 60% 55% at 60% 25%,var(--teal) 0%,var(--teal-deep) 45%,transparent 75%),
    radial-gradient(ellipse 45% 60% at 12% 70%,var(--navy) 0%,transparent 70%),
    radial-gradient(ellipse 50% 50% at 85% 80%,var(--indigo) 0%,transparent 70%),
    linear-gradient(160deg,var(--indigo) 0%,var(--blue) 50%,var(--navy) 100%);}
.title{position:absolute;left:0;right:0;top:26px;text-align:center;color:var(--gold);
  font-size:62px;line-height:68px;letter-spacing:1px;font-weight:400;
  -webkit-text-stroke:2px var(--white);paint-order:stroke fill;
  text-shadow:3px 4px 0 rgba(20,30,70,.55)}
.category{position:absolute;height:38px;display:flex;align-items:center}
.category .pill{height:38px;margin-left:30px;padding:0 12px 0 36px;border-radius:19px;
  background:linear-gradient(var(--orange),var(--orange-deep));border:3px solid var(--rim);
  color:var(--white);font-size:19px;white-space:nowrap;display:flex;align-items:center;
  text-shadow:1px 2px 1px rgba(120,60,0,.5);letter-spacing:.2px}
.category .badge{position:absolute;left:0;top:50%;transform:translateY(-50%);width:60px;height:60px;
  border-radius:50%;background:var(--orange);border:4px solid #f4eee4;
  box-shadow:0 2px 4px rgba(0,0,0,.3);display:flex;align-items:center;justify-content:center;z-index:1}
.badge svg{width:36px;height:36px;fill:none;stroke:var(--white);stroke-width:2.4;stroke-linecap:round;stroke-linejoin:round}
.next{position:absolute;left:1069px;top:595px;width:105px;height:61px;border-radius:12px;
  background:linear-gradient(#ffe14a,#ffc400);border:2px solid #f5a800;
  color:var(--next-red);font-size:30px;display:flex;align-items:center;justify-content:center;
  box-shadow:0 3px 6px rgba(0,0,0,.3)}
</style>
</head>
<body>
<main class="slide">
  <div class="backdrop" role="img" aria-label="Abstract backdrop of flowing teal, blue and navy shapes with shooting stars"></div>

  <h1 class="title">THiS QUiZ CONTAiNS<br>THE FOLLOWiNG CATEGORiES:</h1>

  <div class="category" style="left:44px;top:285px">
    <span class="badge"><svg viewBox="0 0 36 36"><path d="M4 9h11c2 0 3 1 3 3v17c0-2-1-3-3-3H4z"/><path d="M32 9H21c-2 0-3 1-3 3v17c0-2 1-3 3-3h11z"/></svg></span>
    <span class="pill">GENERAL KNOWLEDGE</span>
  </div>
  <div class="category" style="left:44px;top:361px">
    <span class="badge"><svg viewBox="0 0 36 36"><circle cx="18" cy="18" r="13"/><circle cx="18" cy="11" r="3"/><circle cx="18" cy="25" r="3"/><circle cx="11" cy="18" r="3"/><circle cx="25" cy="18" r="3"/></svg></span>
    <span class="pill">ONE WORD MOViE TiTLES</span>
  </div>
  <div class="category" style="left:44px;top:437px">
    <span class="badge"><svg viewBox="0 0 36 36"><rect x="4" y="7" width="22" height="20" rx="2"/><path d="M4 13h22M9 4v5M21 4v5"/><circle cx="26" cy="26" r="7"/><path d="M26 22v4l3 2"/></svg></span>
    <span class="pill">NAME THAT YEAR - 2001-2010 EDiTiON (EACH YEAR iS REPRESENTED)</span>
  </div>
  <div class="category" style="left:44px;top:526px">
    <span class="badge"><svg viewBox="0 0 36 36" style="fill:var(--white);stroke:none"><circle cx="18" cy="12" r="7"/><path d="M5 32c0-8 6-12 13-12s13 4 13 12z"/></svg></span>
    <span class="pill">PiCTURE ROUND - ONE LETTER LOGOS - NAME THE BRAND/COMPANY</span>
  </div>
  <div class="category" style="left:44px;top:602px">
    <span class="badge"><svg viewBox="0 0 36 36"><path d="M13 27V8l17-4v19"/><circle cx="9" cy="27" r="4"/><circle cx="26" cy="23" r="4"/></svg></span>
    <span class="pill">AUDiO ROUND - DUETS - NAME THE SONG AND BOTH ARTiSTS</span>
  </div>

  <div class="category" style="left:740px;top:285px">
    <span class="badge"><svg viewBox="0 0 36 36"><circle cx="18" cy="18" r="14"/><ellipse cx="18" cy="18" rx="6" ry="14"/><path d="M4 18h28M7 11h22M7 25h22"/></svg></span>
    <span class="pill">HEY MOM&nbsp; I GOT AN “A” iN GEOGRAPHY!</span>
  </div>
  <div class="category" style="left:740px;top:364px">
    <span class="badge"><svg viewBox="0 0 36 36"><path d="M7 12h17v19H7z"/><path d="M24 16h4v10h-4"/><path d="M7 12c0-5 4-6 8-5 2-2 7-2 9 2v3"/><path d="M12 17v10M19 17v10"/></svg></span>
    <span class="pill">MMMMM’...BEER</span>
  </div>
  <div class="category" style="left:740px;top:443px">
    <span class="badge"><svg viewBox="0 0 36 36"><path d="M10 5h16v8a8 8 0 0 1-16 0z"/><path d="M10 8H5c0 5 2 8 6 8M26 8h5c0 5-2 8-6 8"/><path d="M18 21v6M12 31h12"/></svg></span>
    <span class="pill">FiNAL TRiViA ROUND</span>
  </div>
  <div class="category" style="left:740px;top:522px">
    <span class="badge"><svg viewBox="0 0 36 36"><ellipse cx="15" cy="22" rx="11" ry="5"/><path d="M4 22v3c0 3 5 5 11 5s11-2 11-5v-3"/><ellipse cx="22" cy="14" rx="10" ry="5" transform="rotate(25 22 14)"/></svg></span>
    <span class="pill">TiE BREAKER QUESTiON</span>
  </div>

  <div class="next">NEXT</div>
</main>
</body>
</html>
```